Business cards for start-up accounting firm

I'm looking for a double sided business card ready for upload into Lumo print or similar print providers with no modification required by me.
I'm looking for something simple as i think cards that are too 'busy' actually detract from the message. I have some thoughts but more than happy to see what comes up. The logo i have came out of left field and i love it the moment i saw it!

My thoughts:

Side 1: Just the logo, perhaps on a dark grey or charcoal background to make the logo colours stand out?

Side 2: The call to action from me website 'Looking for a more relaxed, friendly and interactive relationship with your accountant?' with my contact information
Name: Gus Tarrow
Email: gus@ledgerowl.com.au
Website: www.ledgerowl.com.au
Phone: 1300 762 349

The call to action needs to be the first thing they see when they look at side 2. If it helps to know what we do and how we do it there is a draft website at www.ledgerowl.com.au

Like i said, happy to consider anything that comes up :)

Target Market(s)

i'm targeting small business owners who experience a lot of stress around finacial reporting and have had bad experiences with accountants in the past.

Industry/Entity Type

Accounting

Contact Information for Business Card

Contained in the Description

Font styles to use
Serif
Sans Serif
Other font styles liked:
• See logo files attached

Colors
474747

Requirements
Must have
• My logo, slogan and contact information

```html
<!DOCTYPE html>
<html lang="en">
<head>
<meta charset="utf-8">
<title>Ledger Owl – Business Cards</title>
<link href="https://fonts.googleapis.com/css2?family=PT+Sans:wght@400;700&display=swap" rel="stylesheet">
<style>
  :root {
    --backdrop-light: #0d8ccd;
    --backdrop-dark: #0b6796;
    --charcoal: #333333;
    --brand-yellow: #f6d20d;
    --brand-purple: #7d2a72;
    --slogan-lilac: #b680b0;
    --card-white: #ffffff;
  }
  * { margin: 0; padding: 0; box-sizing: border-box; }
  html, body { width: 1200px; height: 1000px; overflow: hidden; }
  body {
    position: relative;
    font-family: "PT Sans", sans-serif;
    background: radial-gradient(ellipse at 30% 45%, var(--backdrop-light) 0%, var(--backdrop-dark) 90%);
  }

  .card {
    position: absolute;
    left: 352px;
    width: 496px;
    height: 276px;
    box-shadow: 2px 3px 5px rgba(0,0,0,.35);
  }
  .card-face { position: absolute; inset: 0; }

  /* Front */
  .card--front { top: 203px; background: var(--brand-yellow); border-radius: 44px 3px 44px 3px; }
  .card--front .card-face { background: var(--charcoal); border-radius: 78px 3px 78px 3px; left: 6px; bottom: 6px; }

  /* Back */
  .card--back { top: 521px; background: var(--brand-purple); border-radius: 3px 44px 3px 44px; }
  .card--back .card-face { background: var(--card-white); border-radius: 3px 78px 3px 78px; right: 6px; bottom: 6px; }

  .brand-name {
    position: absolute;
    left: 0; right: 0;
    text-align: center;
    font-weight: 700;
    letter-spacing: 1px;
    white-space: nowrap;
  }
  .brand-name--front { top: 100px; font-size: 64px; line-height: 1; color: var(--brand-yellow); }
  .brand-name--back { top: 40px; font-size: 38px; line-height: 1; color: var(--brand-purple); }

  .slogan {
    position: absolute;
    left: 0; right: 0;
    display: flex;
    align-items: center;
    justify-content: center;
    gap: 10px;
    text-transform: uppercase;
    white-space: nowrap;
  }
  .slogan::before, .slogan::after { content: ""; height: 1px; background: currentColor; }
  .slogan--front { top: 198px; font-size: 14px; letter-spacing: 1.4px; color: var(--slogan-lilac); }
  .slogan--front::before, .slogan--front::after { width: 36px; }
  .slogan--back { top: 99px; font-size: 8.5px; letter-spacing: .8px; color: var(--charcoal); }
  .slogan--back::before, .slogan--back::after { width: 20px; background: var(--brand-purple); }

  .contact-list {
    position: absolute;
    right: 261px;
    top: 143px;
    list-style: none;
    text-align: right;
    color: var(--brand-purple);
    font-size: 15.5px;
  }
  .contact-item {
    display: flex;
    align-items: center;
    justify-content: flex-end;
    gap: 9px;
    height: 25px;
  }
  .contact-item--name { font-weight: 700; }
  .contact-icon {
    width: 21px; height: 19px;
    border-radius: 6px;
    background: var(--brand-purple);
    display: flex; align-items: center; justify-content: center;
  }
  .contact-icon svg { width: 13px; height: 13px; }

  .divider {
    position: absolute;
    left: 250px;
    top: 146px;
    width: 2px;
    height: 76px;
    background: var(--brand-purple);
  }
  .divider::after {
    content: "";
    position: absolute;
    left: 2px; top: 37px;
    border-left: 5px solid var(--brand-purple);
    border-top: 4px solid transparent;
    border-bottom: 4px solid transparent;
  }

  .call-to-action {
    position: absolute;
    left: 262px;
    top: 141px;
    font-size: 16px;
    line-height: 21px;
    color: var(--brand-purple);
  }
</style>
</head>
<body>

  <section class="card card--front" aria-label="Business card front">
    <div class="card-face">
      <div class="brand-name brand-name--front">LEDGER OWL</div>
      <div class="slogan slogan--front">Less stress, more success</div>
    </div>
  </section>

  <section class="card card--back" aria-label="Business card back">
    <div class="card-face">
      <div class="brand-name brand-name--back">LEDGER OWL</div>
      <div class="slogan slogan--back">Less stress, more success</div>

      <ul class="contact-list">
        <li class="contact-item contact-item--name">Gus Tarrow
          <span class="contact-icon"><svg viewBox="0 0 16 16" fill="#fff"><circle cx="8" cy="5" r="3.2"/><path d="M2 15c0-3.6 2.7-5.6 6-5.6s6 2 6 5.6z"/></svg></span>
        </li>
        <li class="contact-item">1300 762 349
          <span class="contact-icon"><svg viewBox="0 0 16 16" fill="#fff"><path d="M8 1a5 5 0 0 0-5 5c0 3.6 5 9 5 9s5-5.4 5-9a5 5 0 0 0-5-5zm0 7a2 2 0 1 1 0-4 2 2 0 0 1 0 4z"/></svg></span>
        </li>
        <li class="contact-item">www.ledgerowl.com.au
          <span class="contact-icon"><svg viewBox="0 0 16 16" fill="none" stroke="#fff" stroke-width="1.8"><rect x="1.5" y="2" width="13" height="9" rx="1"/><path d="M8 11v3M5 14.5h6"/></svg></span>
        </li>
        <li class="contact-item">gus@ledgerowl.com.au
          <span class="contact-icon"><svg viewBox="0 0 16 16" fill="none" stroke="#fff" stroke-width="1.6"><rect x="1.5" y="3.5" width="13" height="9" rx="1"/><path d="M1.5 4l6.5 5 6.5-5"/></svg></span>
        </li>
      </ul>

      <div class="divider"></div>

      <p class="call-to-action">Looking for<br>a more relaxed, friendly<br>and interactive relationship<br>with your accountant?</p>
    </div>
  </section>

</body>
</html>
```